Simple and clean poster/flyer design needed for public speaker!

SIMPLE AND CLEAN DESIGN NEEDED FOR POSTER/FLYER

I AM a public speaker based in London (www.corvanlethby.com)
and I would like to have a custom-made flyer/poster
(preferably in adobe CS4 template format) that I con customize (just changing the text) for my various speeches, topics and locations

I am looking for something very simple and clean.
NO extravagance or crowded poster, but a rather beautiful clean and eye-catching design that clearly informs people what i am talking about, where and when.

Go to my website www.corvanlethby.com
to see the colour scheme and style that I like
my poster should be like the website, similar colours, logo, clean, simple and clear.

Summary

(1) simple and clean design
(2) design that fits my brand (see website)
(3) clear and eye-catching to promote my speeches
(4) customizable for my various talks, by simply chancing the text (Please Adobe Photoshop CS4 template format)
(5)in A3, A4, A5, A6 sizes, so i can use it for both flyers and small posters

ADDITIONS

BIG BOLD HEADLINE TO GRAP ATTENTION, greatest prominence

sub headline to explain, smaller than the headline, but still prominent on the poster

just a few bullet points to list the benefits and answer the “whats in for me”-question
this is for people who are already interested and continue reading, medium prominence.

WHERE, WHEN, HOW MUCH-information, in the lower section of the poster, little text, but clearly visible

only one point of CONTACT on my poster “www.corvanlethby.com”, bit big and clear so that it is very prominent

little text, effectively used
LESS IS MORE
Updates

contact me regarding logo files and any questions you may have!

for the logo files go to

https://share.dropvaultex.net/f/x.aspx?k=41c07d2e9ab35f18c6d2

click on the folder "logo pack" to see the files

thanks for your interest. hope to see great designs!
I am really looking forward to it
if you have any questions, please do not hesitate to ask

Kind Regards
Corvan
 

• Simple, clean design, text sparingly used.

• The mood should be light-hearted, calm, bright, simple and friendly, comic like

• a lot of white space, calling more attention to the content

• a light blue, dark blue, white and black colour scheme as seen on the homepage (www.corvanlethby.com) please use the exact same colours as seen on the homepage.

White being most predominant, 2 different blue used to highlight something, black for text on white background.

• One graphic would be cool, as long as it is blue. It could be waves-like graphic, or something like the white pattern in the background, in my case just in blue on white background > http://www.quillmereretreathouse.org/., I do not mean exactly this graphic and not that crowded but a simple single graphic in blue as long as it fits the theme and feel of my poster

Top o f the poster

• (a )One short bold headline (TALK TITLE) with a sub-headline below it (hook)

• or (b) headline as question (…....?) and below sub-headline offering the solution (my talk ;-) of course)

• 3 benefits as on homepage, that I can adapt for each talk (bottom right of my start site “what are you looking for?” either blue on white, or as in the page white on blue...whatever looks better and fits the design). Not sure how that looks, and if to include it!

• the bottom of the poster will have “Where”-information “when”-information “ticket price” info

• contact at the very bottom...for more into or to purchase tickets (my website and email)

If you have any questions or need clarification please write me!

Requirements
Must have
• lot of white space
• less is more - simple design
• little text, little graphics- only used when necessary to greatest effect.
• light, friendly, modern feel
• blue-color scheme

```html
<!DOCTYPE html>
<html lang="en">
<head>
<meta charset="utf-8">
<title>Living Without Strain – Poster</title>
<link rel="stylesheet" href="https://fonts.googleapis.com/css2?family=Archivo+Black&family=Open+Sans:wght@400;700;800&display=swap">
<style>
  :root {
    --stage: #a9aaac;
    --paper: #ffffff;
    --navy: #1b2035;
    --blue: #0a9fe0;
    --sky: #6bb4d8;
    --pale: #bfe3f6;
    --grey-text: #7c808b;
  }
  * { box-sizing: border-box; margin: 0; padding: 0; }
  html, body { width: 1200px; height: 900px; overflow: hidden; }
  body { background: var(--stage); position: relative; font-family: "Open Sans", Arial, sans-serif; }

  .poster {
    position: absolute; left: 320px; top: 50px;
    width: 560px; height: 760px;
    background: var(--paper);
    overflow: hidden;
  }
  .accent-bar {
    position: absolute; left: 14px; top: 48px;
    width: 10px; height: 300px; background: var(--blue);
  }
  .burst-graphic {
    position: absolute; left: 330px; top: 110px;
    width: 230px; height: 400px;
  }
  .headline {
    position: absolute; left: 38px; top: 18px;
    font-family: "Archivo Black", "Arial Black", sans-serif;
    font-size: 78px; line-height: 0.95; letter-spacing: -1px;
    color: var(--navy);
  }
  .subheadline {
    position: absolute; left: 40px; top: 268px;
    font-weight: 800; font-size: 25px; line-height: 1.08;
    color: var(--navy);
  }
  .benefits { position: absolute; left: 40px; top: 352px; color: var(--navy); }
  .benefits-title { font-weight: 700; font-size: 21px; line-height: 1.3; color: var(--grey-text); margin-bottom: 2px; }
  .benefits-list { list-style: none; font-weight: 800; font-size: 21px; line-height: 1.22; }
  .benefits-list li { display: flex; }
  .benefits-list .num { width: 30px; flex: none; }

  .event-band {
    position: absolute; left: 20px; right: 14px; top: 505px; height: 120px;
    background: var(--navy); color: #fff;
    font-family: "Archivo Black", "Arial Black", sans-serif;
    font-size: 23px; line-height: 1.25; padding: 16px 0 0 28px;
  }
  .event-band .sep { color: var(--blue); }

  .info-strip {
    position: absolute; left: 20px; right: 14px; top: 632px; height: 26px;
    background: var(--sky); color: #fff;
    font-weight: 700; font-size: 12px; line-height: 14px; padding: 6px 0 0 28px; letter-spacing: 0.2px;
  }
  .contact-band {
    position: absolute; left: 20px; right: 14px; top: 660px; height: 72px;
    background: var(--blue); color: #fff; padding: 4px 0 0 28px;
  }
  .website { font-weight: 800; font-size: 34px; line-height: 1.15; }
  .role { font-size: 14px; letter-spacing: 0.5px; color: #d8f0fc; }
  .email { position: absolute; right: 18px; top: 50px; font-size: 10px; line-height: 12px; }
  .footer-strip {
    position: absolute; left: 20px; right: 14px; top: 733px; height: 7px; background: var(--sky);
  }
</style>
</head>
<body>
  <main class="poster">
    <svg class="burst-graphic" role="img" aria-label="Glowing blue stick figure with arms raised, light rays bursting outward" viewBox="0 0 230 400">
      <defs>
        <radialGradient id="burstGlow" cx="0.55" cy="0.55" r="0.6">
          <stop offset="0" stop-color="#7fcdf2"/>
          <stop offset="0.45" stop-color="#bfe3f6"/>
          <stop offset="1" stop-color="#ffffff" stop-opacity="0"/>
        </radialGradient>
      </defs>
      <rect width="230" height="400" fill="url(#burstGlow)"/>
    </svg>

    <div class="accent-bar"></div>

    <h1 class="headline">Living<br>Without<br>Strain</h1>
    <p class="subheadline">Free yourself from fear<br>and worry... forever</p>

    <section class="benefits">
      <h2 class="benefits-title">What are you looking for?</h2>
      <ol class="benefits-list">
        <li><span class="num">1.</span>Improved self-esteem</li>
        <li><span class="num">2.</span>Inner peace and calm</li>
        <li><span class="num">3.</span>Greater purpose and<br>meaning in life</li>
      </ol>
    </section>

    <section class="event-band">
      24.09.10 <span class="sep">//</span> 09:00-16:00 <span class="sep">//</span><br>
      WRENFIELD HALL, LONDON <span class="sep">//</span><br>
      TICKETS £12 <span class="sep">//</span>
    </section>

    <div class="info-strip">FOR MORE INFO AND TO BUY TICKETS, VISIT:</div>
    <section class="contact-band">
      <div class="website">www.corvanlethby.com</div>
      <div class="role">SPIRITUAL SPEAKER</div>
      <div class="email">contact@corvanlethby.com</div>
    </section>
    <div class="footer-strip"></div>
  </main>
</body>
</html>
```